Cleaning and Maintenance Business card design

i provide a service which includes;
Professional Window Cleaning
Lawn Mowing
Gardening
Painting
Rubbish Removal
Commercial Cleaning
Property & Ground Maintenance
Pensioner discounts apply
Call now for an inquiry and free quote
`Double sided` (willing to pay any extra)
i would like a design that is not too crowded and straight to the point.
i want the reader to know exactly what the business is about from one glance.
i would like the logo to communicate the businesses 3 main aspects (window cleaning, lawn mowing, and Cleaning)
Thanks.
Contact Information for Business Card
Business name : Brick 4 Leaf*
* with subline 'And Everything In Between' (smaller font)
Name: Tom Varkonisky
Mobile: 0417 582 903
Email: t.varkonisky@mailbrook.net
ABN: 47 915 230 861
`Double Sided`
Logo Text
Brick 4 Leaf

```html
<!DOCTYPE html>
<html lang="en">
<head>
<meta charset="utf-8">
<title>Brick 4 Leaf – Business Card</title>
<link rel="stylesheet" href="https://fonts.googleapis.com/css2?family=Noto+Serif:wght@400&family=Open+Sans:wght@400&family=Orbitron:wght@700&family=Poiret+One&family=Advent+Pro:wght@400;500;600&display=swap">
<style>
  :root {
    --brand-blue: #0071bc;
    --sky-blue: #29abe2;
    --leaf-green: #8cc63f;
    --grass-green: #39b54a;
    --charcoal: #333333;
    --pale-strip: #dfe6ec;
    --ink: #222222;
    --grey-text: #444444;
    --white: #ffffff;
  }
  * { margin: 0; padding: 0; box-sizing: border-box; }
  html, body { width: 1200px; height: 900px; overflow: hidden; background: var(--white); }
  .canvas { position: relative; width: 1200px; height: 900px; }

  .view-label {
    position: absolute;
    font-family: "Poiret One", sans-serif;
    font-size: 11px;
    letter-spacing: 0.5px;
    color: var(--ink);
    text-align: right;
  }
  .view-label--front { right: 703px; top: 118px; }
  .view-label--back { right: 127px; top: 210px; }

  /* Front side */
  .card-front {
    position: absolute; left: 154px; top: 141px;
    width: 341px; height: 521px;
    background: var(--brand-blue);
    border: 1px solid var(--charcoal);
    overflow: hidden;
  }
  .card-front__strip {
    position: absolute; left: 0; top: 34px; width: 100%; height: 9px;
    background: var(--pale-strip);
  }
  .card-front__mark {
    position: absolute; left: 0; top: 150px; width: 100%;
    text-align: center;
    font-family: "Noto Serif", serif;
    font-weight: 400;
    font-size: 40px;
    color: var(--white);
  }
  .card-front__mark::before {
    content: ""; display: block; width: 70px; height: 70px;
    margin: 0 auto 16px; border-radius: 50%;
    background: var(--white);
  }
  .services {
    position: absolute; left: 0; bottom: 0; width: 100%; height: 134px;
    background: var(--charcoal);
    font-family: "Orbitron", sans-serif;
    font-weight: 700;
  }
  .services__title {
    position: absolute; left: 12px; top: 12px;
    font-size: 14px; font-weight: 700; color: var(--white); letter-spacing: 0.3px;
  }
  .services__list {
    position: absolute; right: 8px; top: 31px;
    list-style: none; text-align: right;
    font-size: 14.5px; line-height: 17.2px; letter-spacing: 0.5px;
    white-space: nowrap;
  }
  .services__item--blue { color: var(--brand-blue); }
  .services__item--green { color: var(--leaf-green); }
  .services__item--sky { color: var(--sky-blue); }

  /* Back side */
  .card-back {
    position: absolute; left: 600px; top: 231px;
    width: 476px; height: 306px;
    background: var(--white);
    border: 1px solid var(--ink);
    overflow: hidden;
  }
  .wordmark {
    position: absolute; left: 0; top: 18px; width: 100%;
    text-align: center;
    font-family: "Noto Serif", serif;
    font-weight: 400;
    font-size: 58px; line-height: 1;
    color: var(--brand-blue);
    letter-spacing: 0.5px;
  }
  .tagline {
    position: absolute; right: 16px; top: 81px;
    font-family: "Poiret One", sans-serif;
    font-size: 14px; color: var(--ink); letter-spacing: 0.3px;
  }
  .divider {
    position: absolute; left: 234px; top: 90px;
    width: 3px; height: 85px; background: #000;
  }
  .contact {
    position: absolute; top: 117px;
    font-family: "Advent Pro", sans-serif;
    font-size: 16px; line-height: 20px; letter-spacing: 0.4px;
  }
  .contact--person { left: 12px; width: 216px; text-align: center; }
  .contact--numbers { left: 270px; }
  .contact__name { color: var(--sky-blue); font-weight: 600; text-transform: uppercase; }
  .contact__email { color: var(--grey-text); }
  .contact__phone { color: var(--grass-green); font-weight: 600; padding-left: 2px; }
  .contact__abn { color: var(--sky-blue); font-weight: 600; }
  .card-back__band {
    position: absolute; left: 0; bottom: 0; width: 100%; height: 116px;
    background: var(--charcoal);
  }
  .card-back__cta {
    position: absolute; left: 12px; top: 45px;
    font-family: "Open Sans", sans-serif;
    font-size: 19.5px; color: var(--white);
    white-space: nowrap;
  }
  .card-back__mark {
    position: absolute; right: 10px; top: 22px; width: 84px;
    text-align: center;
    font-family: "Noto Serif", serif;
    font-weight: 400;
    font-size: 13px; line-height: 1.2; color: var(--white);
    white-space: nowrap;
  }
  .card-back__mark::before {
    content: ""; display: block; width: 38px; height: 38px;
    margin: 0 auto 8px; border-radius: 50%;
    background: var(--white);
  }
</style>
</head>
<body>
<main class="canvas">
  <p class="view-label view-label--front">FRONT VIEW</p>
  <section class="card-front" aria-label="Card front">
    <div class="card-front__strip"></div>
    <p class="card-front__mark">Brick 4 Leaf</p>
    <div class="services">
      <h2 class="services__title">SERVICES</h2>
      <ul class="services__list">
        <li class="services__item--blue">Professional Window Cleaning</li>
        <li class="services__item--green">Lawn Mowing &amp; Gardening</li>
        <li class="services__item--sky">Painting &amp; Rubbish Removal</li>
        <li class="services__item--blue">Commercial Cleaning</li>
        <li class="services__item--green">Property &amp; Ground Maintenance</li>
      </ul>
    </div>
  </section>

  <p class="view-label view-label--back">BACK VIEW</p>
  <section class="card-back" aria-label="Card back">
    <h1 class="wordmark">BRICK 4 LEAF</h1>
    <p class="tagline">And everything in between</p>
    <div class="contact contact--person">
      <p class="contact__name">Tom Varkonisky</p>
      <p class="contact__email">t.varkonisky@mailbrook.net</p>
    </div>
    <div class="divider"></div>
    <div class="contact contact--numbers">
      <p class="contact__phone">0417 582 903</p>
      <p class="contact__abn">47 915 230 861 (ABN)</p>
    </div>
    <div class="card-back__band">
      <p class="card-back__cta">Call now for an inquiry and free quote</p>
      <p class="card-back__mark">Brick 4 Leaf</p>
    </div>
  </section>
</main>
</body>
</html>
```